Children's Educational Software - Login Screens

We need graphics for some basic login pages. The main requirements are a background image, buttons and background overlay (box for login fields and app icons). Must utilize responsive design for various resolutions and devices. The mock-up file provides an example of the direction we are wanting to go. The app page will require a version of the background that extends down using a solid colour. One idea would be to add some flowers, bees, etc. to help add some life to the bottom half. I like the idea of clouds and grass, but am open to anything.
Updates

Target Market(s)

Elementary teachers and young children

Coding

Coded - Design and coding required

Number of Pages Required

2 page

Font styles to use
Sans Serif

Requirements
Must have
• Responsive design for various resolutions and devices
Nice to have
• clouds, grass, new app icons if current icons don't fit with new design

```html
<!DOCTYPE html>
<html lang="en">
<head>
<meta charset="utf-8">
<title>Skillbee Academy – Login Screens</title>
<link href="https://fonts.googleapis.com/css2?family=Roboto:wght@300;400;500;700&display=swap" rel="stylesheet">
<style>
:root{
  --sky:#4aa8e6;
  --sky-deep:#3b98da;
  --grass:#6cbd3a;
  --grass-deep:#4f9e2a;
  --school:#1a6fc4;
  --teacher:#5aaa3c;
  --student:#f47b20;
  --admin:#f5b800;
  --ink:#1f2d5a;
  --muted:#5d6b82;
  --line:#e3e7ee;
  --field:#c9d1dc;
  --title:#1c3f6e;
  --white:#ffffff;
}
*{box-sizing:border-box;margin:0;padding:0}
html,body{width:1200px;height:4392px;overflow:hidden;background:var(--white)}
body{position:relative;font-family:"Roboto",Arial,sans-serif;color:var(--ink)}
.brand-top{position:absolute;left:67px;top:96px;display:flex;align-items:center;gap:10px;font-size:31px;font-weight:500;color:var(--school)}
.brand-top .dot{width:26px;height:26px;border-radius:50%;background:var(--school)}
.section-title{position:absolute;left:0;width:1200px;text-align:center;font-size:20px;font-weight:700;letter-spacing:2.4px;color:var(--title)}

/* Desktop screen */
.screen{position:absolute;left:103px;width:977px;height:550px;overflow:hidden;background:var(--white);box-shadow:0 0 0 1px var(--line)}
.hero{position:absolute;left:0;top:0;width:591px;height:550px;background:linear-gradient(180deg,var(--sky) 0%,var(--sky-deep) 100%);color:var(--white)}
.hero .brand{position:absolute;left:57px;top:58px;display:flex;align-items:center;gap:8px;font-size:16px;font-weight:500}
.hero .brand .dot{width:14px;height:14px;border-radius:50%;background:var(--white)}
.hero h1{position:absolute;left:57px;top:140px;font-size:24px;font-weight:500;line-height:29px}
.hero h2{position:absolute;left:57px;top:203px;font-size:25px;font-weight:300}
.hero p{position:absolute;left:57px;top:256px;width:305px;font-size:11.4px;line-height:17px;font-weight:400}
.hero .more{position:absolute;left:57px;top:374px;font-size:11.4px;font-weight:500}
.mascot{position:absolute;left:393px;top:84px;width:150px;height:214px;border-radius:48% 48% 44% 44%;background:radial-gradient(circle at 50% 40%,#ffd23f 0%,#f4b400 60%,rgba(244,180,0,0) 72%)}
.hive{position:absolute;left:490px;top:330px;width:100px;height:130px;border-radius:40% 40% 48% 48%;background:radial-gradient(circle at 45% 55%,#ffcf2e 0%,#f2a900 62%,rgba(242,169,0,0) 75%)}
.grass{position:absolute;left:0;bottom:0;width:591px;height:110px;background:linear-gradient(180deg,rgba(108,189,58,0) 0%,var(--grass) 35%,var(--grass-deep) 100%)}

.form{position:absolute;left:591px;top:0;width:300px;height:550px;border-right:1px solid var(--line)}
.form .emblem{position:absolute;left:0;top:58px;width:300px;text-align:center;color:var(--accent)}
.form .emblem svg{width:58px;height:58px}
.form .heading{position:absolute;left:0;top:128px;width:300px;text-align:center;font-size:11.5px;font-weight:700;letter-spacing:1px;color:var(--title)}
.form .rule{position:absolute;left:0;top:202px;width:300px;height:1px;background:var(--line)}
.form .lead{position:absolute;left:41px;top:243px;width:220px;font-size:9.2px;line-height:15px;font-weight:700;color:var(--title)}
.form .find{position:absolute;left:41px;top:300px;font-size:9.2px;font-weight:500;color:var(--school)}
.field{position:absolute;left:41px;width:221px;height:34px;border:1px solid var(--field);border-radius:3px;font-size:9.2px;color:#9aa5b4;padding:11px 14px}
.pick{position:absolute;left:41px;top:366px;width:221px;display:flex;justify-content:flex-end;align-items:center;gap:8px;font-size:9.2px;color:var(--muted)}
.pick i{width:14px;height:14px;border:1px solid var(--field);border-radius:2px}
.btn{position:absolute;left:41px;top:406px;width:221px;height:34px;border-radius:3px;background:var(--accent);color:var(--white);font-size:9.2px;font-weight:500;display:flex;align-items:center;justify-content:center}
.note{position:absolute;left:41px;top:472px;width:230px;font-size:8.8px;line-height:17px;color:var(--muted)}
.note b{color:var(--title)}

.rail{position:absolute;left:891px;top:0;width:86px;height:550px}
.rail .item{position:absolute;left:0;width:86px;height:74px;display:flex;flex-direction:column;align-items:center;justify-content:center;gap:6px;font-size:8.5px;font-weight:500;color:var(--title);text-align:center;line-height:10px}
.rail .item svg{width:26px;height:26px}
.rail .school{top:0;color:var(--school)}
.rail .teacher{top:76px;color:var(--teacher)}
.rail .student{top:150px;color:var(--student)}
.rail .admin{top:222px;color:var(--admin)}
.rail .item span{color:var(--title)}
.rail .item.active{background:var(--accent);color:var(--white)}
.rail .item.active span{color:var(--white)}
.rail .help{top:390px;height:64px;color:#6e7785}
.rail .support{top:468px;height:64px;color:#6e7785}
.rail .help svg,.rail .support svg{width:20px;height:20px}

/* Mobile screens */
.phone{position:absolute;top:3753px;width:205px;height:370px;overflow:hidden;background:var(--white);box-shadow:0 0 0 1px var(--line)}
.phone .bar{position:absolute;left:0;top:0;width:205px;height:27px;background:var(--school);color:var(--white);font-size:8px;font-weight:500;display:flex;align-items:center;justify-content:space-between;padding:0 10px}
.phone .bar .brand{display:flex;align-items:center;gap:4px}
.phone .bar .brand i{width:7px;height:7px;border-radius:50%;background:var(--white)}
.phone .bar .grid{width:10px;height:10px;background:linear-gradient(90deg,var(--white) 40%,transparent 40% 60%,var(--white) 60%);opacity:.7}
.phone .top{position:absolute;left:0;top:42px;width:205px;display:flex;justify-content:space-between;align-items:flex-start;padding:0 18px}
.phone .mini{display:flex;flex-direction:column;align-items:center;gap:2px;font-size:4.5px;color:var(--title);color:#6e7785;width:30px;text-align:center}
.phone .mini svg{width:10px;height:10px}
.phone .main{display:flex;flex-direction:column;align-items:center;gap:4px;font-size:5.5px;font-weight:700;letter-spacing:.4px;color:var(--title)}
.phone .main svg{width:26px;height:26px;color:var(--accent)}
.phone .rule{position:absolute;left:0;top:110px;width:205px;height:1px;background:var(--line)}
.phone .lead{position:absolute;left:20px;top:128px;width:130px;font-size:5px;line-height:8px;font-weight:700;color:var(--title)}
.phone .find{position:absolute;left:20px;top:152px;font-size:5px;color:var(--school)}
.phone .field{left:20px;width:165px;height:14px;font-size:4.5px;padding:4px 6px;border-radius:2px}
.phone .pick{left:20px;width:165px;top:202px;font-size:4.5px;gap:4px}
.phone .pick i{width:6px;height:6px}
.phone .btn{left:20px;top:224px;width:165px;height:15px;font-size:4.5px;border-radius:2px}
.phone .note{left:20px;top:256px;width:120px;font-size:4.3px;line-height:8px}
.phone .scene{position:absolute;left:0;top:290px;width:205px;height:48px;background:linear-gradient(180deg,rgba(108,189,58,0) 0%,var(--grass) 60%,var(--grass-deep) 100%)}
.phone .scene i{position:absolute;right:20px;top:-20px;width:34px;height:42px;border-radius:50%;background:radial-gradient(circle,#ffd23f 0%,#f4b400 55%,rgba(244,180,0,0) 72%)}
.phone .tabs{position:absolute;left:0;top:338px;width:205px;height:32px;background:var(--school);display:flex}
.phone .tab{flex:1;display:flex;flex-direction:column;align-items:center;justify-content:center;gap:2px;font-size:4px;color:var(--white)}
.phone .tab svg{width:10px;height:10px}
.phone .tab.t-school svg{color:var(--white)}
.phone .tab.t-teacher svg{color:#9be07a}
.phone .tab.t-student svg{color:#ffb074}
.phone .tab.t-admin svg{color:var(--admin)}
.phone .tab.active{background:var(--accent)}
.phone .tab.active svg{color:var(--white)}

.accent-school{--accent:var(--school)}
.accent-teacher{--accent:var(--teacher)}
.accent-student{--accent:var(--student)}
</style>
</head>
<body>

<svg width="0" height="0" style="position:absolute" aria-hidden="true">
  <defs>
    <symbol id="ico-school" viewBox="0 0 24 24"><path fill="currentColor" d="M2 12 12 5l10 7v10H2z"/><rect x="10" y="15" width="4" height="7" fill="#fff"/><circle cx="12" cy="11" r="1.8" fill="#fff"/><path d="M12 5V1h4v2h-4" stroke="currentColor" stroke-width="1.2" fill="none"/></symbol>
    <symbol id="ico-teacher" viewBox="0 0 24 24"><rect x="8" y="3" width="15" height="11" rx="1" fill="currentColor"/><circle cx="5" cy="8" r="2.6" fill="currentColor"/><path fill="currentColor" d="M2 12h6l5-3 1 1.5-5 4V22H3z"/></symbol>
    <symbol id="ico-student" viewBox="0 0 24 24"><circle cx="10" cy="5" r="2.8" fill="currentColor"/><path fill="currentColor" d="M7 9h5v6H7zM4 2h2v14h14v3H4z"/><rect x="5" y="19" width="2" height="4" fill="currentColor"/><rect x="17" y="19" width="2" height="4" fill="currentColor"/></symbol>
    <symbol id="ico-admin" viewBox="0 0 24 24"><circle cx="9" cy="6" r="4" fill="currentColor"/><path fill="currentColor" d="M2 21c0-5 3-8 7-8s5 1 6 2v6z"/><circle cx="18" cy="17" r="4.5" fill="none" stroke="currentColor" stroke-width="2.2"/><circle cx="18" cy="17" r="1.4" fill="currentColor"/></symbol>
    <symbol id="ico-info" viewBox="0 0 24 24"><circle cx="12" cy="12" r="11" fill="currentColor"/><rect x="10.6" y="10" width="2.8" height="8" fill="#fff"/><circle cx="12" cy="6.6" r="1.7" fill="#fff"/></symbol>
    <symbol id="ico-help" viewBox="0 0 24 24"><circle cx="12" cy="12" r="11" fill="currentColor"/><path d="M8.6 9a3.4 3.4 0 1 1 4.6 3.2c-1 .4-1.2 1-1.2 2.2" stroke="#fff" stroke-width="2.4" fill="none"/><circle cx="12" cy="18" r="1.5" fill="#fff"/></symbol>
  </defs>
</svg>

<div class="brand-top"><span class="dot"></span>Skillbee Academy</div>

<!-- School login -->
<h2 class="section-title" style="top:250px">SCHOOL LOGIN</h2>
<section class="screen accent-school" style="top:350px">
  <div class="hero">
    <div class="brand"><span class="dot"></span>Skillbee Academy</div>
    <h1>Dedicated Teachers<br>&amp; Skillbee Academy</h1>
    <h2>Creating Brighter Futures</h2>
    <p>Skillbee Academy programs provide engaging, focused instruction in K-6 reading/language arts, math, science and English language learning. Our interactive learning software is ideal for general stream K-6 students, special education, English language learners, response to intervention, and older remedial students.</p>
    <div class="more">Learn more at learn.skillbeeacademy.com</div>
    <div class="mascot" role="img" aria-label="Cartoon bee mascot holding a pointer"></div>
    <div class="hive" role="img" aria-label="Beehive hanging from a tree branch"></div>
    <div class="grass" role="img" aria-label="Green grassy hills with small flowers"></div>
  </div>
  <div class="form">
    <div class="emblem"><svg><use href="#ico-school"/></svg></div>
    <div class="heading">SCHOOL LOGIN</div>
    <div class="rule"></div>
    <div class="lead">Please type your school id to access student dashboard</div>
    <div class="find">Find My School Id?</div>
    <div class="field" style="top:320px">Enter school id here</div>
    <div class="pick">Pick student from the list <i></i></div>
    <div class="btn">LOGIN</div>
    <div class="note"><b>Not a Skillbee Academy subscriber?</b><br>Visit our website to learn more and discover why Skillbee Academy is trusted by over <b>53,000 teachers</b></div>
  </div>
  <nav class="rail">
    <div class="item school active"><svg><use href="#ico-school"/></svg><span>SCHOOL</span></div>
    <div class="item teacher"><svg><use href="#ico-teacher"/></svg><span>TEACHER</span></div>
    <div class="item student"><svg><use href="#ico-student"/></svg><span>STUDENT</span></div>
    <div class="item admin"><svg><use href="#ico-admin"/></svg><span>ADMIN</span></div>
    <div class="item help"><svg><use href="#ico-info"/></svg><span>Quick start<br>guide</span></div>
    <div class="item support"><svg><use href="#ico-help"/></svg><span>Support<br>Page</span></div>
  </nav>
</section>

<!-- Teacher login -->
<h2 class="section-title" style="top:1354px">TEACHER LOGIN</h2>
<section class="screen accent-teacher" style="top:1452px">
  <div class="hero">
    <div class="brand"><span class="dot"></span>Skillbee Academy</div>
    <h1>Dedicated Teachers<br>&amp; Skillbee Academy</h1>
    <h2>Creating Brighter Futures</h2>
    <p>Skillbee Academy programs provide engaging, focused instruction in K-6 reading/language arts, math, science and English language learning. Our interactive learning software is ideal for general stream K-6 students, special education, English language learners, response to intervention, and older remedial students.</p>
    <div class="more">Learn more at learn.skillbeeacademy.com</div>
    <div class="mascot" role="img" aria-label="Cartoon bee mascot holding a pointer"></div>
    <div class="hive" role="img" aria-label="Beehive hanging from a tree branch"></div>
    <div class="grass" role="img" aria-label="Green grassy hills with small flowers"></div>
  </div>
  <div class="form">
    <div class="emblem"><svg><use href="#ico-teacher"/></svg></div>
    <div class="heading">TEACHER LOGIN</div>
    <div class="rule"></div>
    <div class="lead">Please type your username and password to access teacher dashboard</div>
    <div class="field" style="top:302px">Username</div>
    <div class="field" style="top:346px">Password</div>
    <div class="btn">LOGIN</div>
    <div class="note"><b>Not a Skillbee Academy subscriber?</b><br>Visit our website to learn more and discover why Skillbee Academy is trusted by over <b>53,000 teachers</b></div>
  </div>
  <nav class="rail">
    <div class="item school"><svg><use href="#ico-school"/></svg><span>SCHOOL</span></div>
    <div class="item teacher active"><svg><use href="#ico-teacher"/></svg><span>TEACHER</span></div>
    <div class="item student"><svg><use href="#ico-student"/></svg><span>STUDENT</span></div>
    <div class="item admin"><svg><use href="#ico-admin"/></svg><span>ADMIN</span></div>
    <div class="item help"><svg><use href="#ico-info"/></svg><span>Quick start<br>guide</span></div>
    <div class="item support"><svg><use href="#ico-help"/></svg><span>Support<br>Page</span></div>
  </nav>
</section>

<!-- Student login -->
<h2 class="section-title" style="top:2456px">STUDENT LOGIN</h2>
<section class="screen accent-student" style="top:2556px">
  <div class="hero">
    <div class="brand"><span class="dot"></span>Skillbee Academy</div>
    <h1>Dedicated Teachers<br>&amp; Skillbee Academy</h1>
    <h2>Creating Brighter Futures</h2>
    <p>Skillbee Academy programs provide engaging, focused instruction in K-6 reading/language arts, math, science and English language learning. Our interactive learning software is ideal for general stream K-6 students, special education, English language learners, response to intervention, and older remedial students.</p>
    <div class="more">Learn more at learn.skillbeeacademy.com</div>
    <div class="mascot" role="img" aria-label="Cartoon bee mascot holding a pointer"></div>
    <div class="hive" role="img" aria-label="Beehive hanging from a tree branch"></div>
    <div class="grass" role="img" aria-label="Green grassy hills with small flowers"></div>
  </div>
  <div class="form">
    <div class="emblem"><svg><use href="#ico-student"/></svg></div>
    <div class="heading">STUDENT LOGIN</div>
    <div class="rule"></div>
    <div class="lead">Please type your username and password to access student dashboard</div>
    <div class="field" style="top:302px">Username</div>
    <div class="field" style="top:346px">Password</div>
    <div class="btn">LOGIN</div>
    <div class="note"><b>Not a Skillbee Academy subscriber?</b><br>Visit our website to learn more and discover why Skillbee Academy is trusted by over <b>53,000 teachers</b></div>
  </div>
  <nav class="rail">
    <div class="item school"><svg><use href="#ico-school"/></svg><span>SCHOOL</span></div>
    <div class="item teacher"><svg><use href="#ico-teacher"/></svg><span>TEACHER</span></div>
    <div class="item student active"><svg><use href="#ico-student"/></svg><span>STUDENT</span></div>
    <div class="item admin"><svg><use href="#ico-admin"/></svg><span>ADMIN</span></div>
    <div class="item help"><svg><use href="#ico-info"/></svg><span>Quick start<br>guide</span></div>
    <div class="item support"><svg><use href="#ico-help"/></svg><span>Support<br>Page</span></div>
  </nav>
</section>

<!-- Mobile -->
<h2 class="section-title" style="top:3558px">SAMPLE MOBILE</h2>

<section class="phone accent-school" style="left:174px">
  <div class="bar"><span class="brand"><i></i>Skillbee Academy</span><span class="grid"></span></div>
  <div class="top">
    <div class="mini"><svg><use href="#ico-info"/></svg>Quick start guide</div>
    <div class="main"><svg><use href="#ico-school"/></svg>SCHOOL LOGIN</div>
    <div class="mini"><svg><use href="#ico-help"/></svg>Support Page</div>
  </div>
  <div class="rule"></div>
  <div class="lead">Please type your school id to access student dashboard</div>
  <div class="find">Find My School Id?</div>
  <div class="field" style="top:165px">Enter school id here</div>
  <div class="pick">Pick student from the list <i></i></div>
  <div class="btn">LOGIN</div>
  <div class="note"><b>Not a Skillbee Academy subscriber?</b><br>Visit our website to learn more and discover why Skillbee Academy is trusted by over <b>53,000 teachers</b></div>
  <div class="scene" role="img" aria-label="Grass with bee mascot"><i></i></div>
  <nav class="tabs">
    <div class="tab t-school active"><svg><use href="#ico-school"/></svg>SCHOOL</div>
    <div class="tab t-teacher"><svg><use href="#ico-teacher"/></svg>TEACHER</div>
    <div class="tab t-student"><svg><use href="#ico-student"/></svg>STUDENT</div>
    <div class="tab t-admin"><svg><use href="#ico-admin"/></svg>ADMIN</div>
  </nav>
</section>

<section class="phone accent-teacher" style="left:497px">
  <div class="bar"><span class="brand"><i></i>Skillbee Academy</span><span class="grid"></span></div>
  <div class="top">
    <div class="mini"><svg><use href="#ico-info"/></svg>Quick start guide</div>
    <div class="main"><svg><use href="#ico-teacher"/></svg>TEACHER LOGIN</div>
    <div class="mini"><svg><use href="#ico-help"/></svg>Support Page</div>
  </div>
  <div class="rule"></div>
  <div class="lead">Please type your username and password to access teacher dashboard</div>
  <div class="field" style="top:156px">Username</div>
  <div class="field" style="top:178px">Password</div>
  <div class="btn" style="top:206px">LOGIN</div>
  <div class="note" style="top:246px"><b>Not a Skillbee Academy subscriber?</b><br>Visit our website to learn more and discover why Skillbee Academy is trusted by over <b>53,000 teachers</b></div>
  <div class="scene" role="img" aria-label="Grass with bee mascot"><i></i></div>
  <nav class="tabs">
    <div class="tab t-school"><svg><use href="#ico-school"/></svg>SCHOOL</div>
    <div class="tab t-teacher active"><svg><use href="#ico-teacher"/></svg>TEACHER</div>
    <div class="tab t-student"><svg><use href="#ico-student"/></svg>STUDENT</div>
    <div class="tab t-admin"><svg><use href="#ico-admin"/></svg>ADMIN</div>
  </nav>
</section>

<section class="phone accent-student" style="left:817px">
  <div class="bar"><span class="brand"><i></i>Skillbee Academy</span><span class="grid"></span></div>
  <div class="top">
    <div class="mini"><svg><use href="#ico-info"/></svg>Quick start guide</div>
    <div class="main"><svg><use href="#ico-student"/></svg>STUDENT LOGIN</div>
    <div class="mini"><svg><use href="#ico-help"/></svg>Support Page</div>
  </div>
  <div class="rule"></div>
  <div class="lead">Please type your username and password to access student dashboard</div>
  <div class="field" style="top:156px">Username</div>
  <div class="field" style="top:178px">Password</div>
  <div class="btn" style="top:206px">LOGIN</div>
  <div class="note" style="top:246px"><b>Not a Skillbee Academy subscriber?</b><br>Visit our website to learn more and discover why Skillbee Academy is trusted by over <b>53,000 teachers</b></div>
  <div class="scene" role="img" aria-label="Grass with bee mascot"><i></i></div>
  <nav class="tabs">
    <div class="tab t-school"><svg><use href="#ico-school"/></svg>SCHOOL</div>
    <div class="tab t-teacher"><svg><use href="#ico-teacher"/></svg>TEACHER</div>
    <div class="tab t-student active"><svg><use href="#ico-student"/></svg>STUDENT</div>
    <div class="tab t-admin"><svg><use href="#ico-admin"/></svg>ADMIN</div>
  </nav>
</section>

</body>
</html>
```